Need sign/billboard help

I need somone to take my logo and turn it into a sign.
Needs to have: Bright Paws
Hound Play Lodge LLC
319-555-0187
Daycare - Boarding - Learning
Colors to use are in the pictures i included, however feel free to use different shades of gray. i Don't necessary want to background to be one solid color.
Also this sing will be a rectangle (4'x8')
Industry/Entity Type
Daycare
Look and feel
Each slider illustrates characteristics of the customer's brand and the style your logo design should communicate.

```html
<!DOCTYPE html>
<html lang="en">
<head>
<meta charset="utf-8">
<title>Bright Paws – Hound Play Lodge LLC Sign</title>
<link rel="stylesheet" href="https://fonts.googleapis.com/css2?family=Saira:wdth,wght@100..125,500..900&display=swap">
<style>
  :root {
    --lime: #a6cd3a;
    --lime-deep: #8fc13c;
    --lime-pale: #d9e94c;
    --tick-green: #8dc63f;
    --steel-gray: #6b6d70;
    --ink: #1a1a1a;
    --paper: #ffffff;
  }
  * { margin: 0; padding: 0; box-sizing: border-box; }
  html, body { width: 1200px; height: 600px; overflow: hidden; background: var(--paper); }
  .sign {
    position: relative;
    width: 1200px;
    height: 600px;
    overflow: hidden;
    font-family: "Saira", sans-serif;
    background: linear-gradient(160deg, var(--lime-deep) 0%, var(--lime) 40%, var(--lime-pale) 100%);
  }
  .sign__glow {
    position: absolute;
    left: 0;
    top: 36px;
    width: 1200px;
    height: 330px;
    background: linear-gradient(90deg, rgba(255,255,255,0) 10%, rgba(255,255,255,0.8) 44%, var(--paper) 60%);
    -webkit-mask-image: linear-gradient(180deg, #000 78%, transparent 100%);
    mask-image: linear-gradient(180deg, #000 78%, transparent 100%);
  }
  .mascot-art {
    position: absolute;
    left: 24px;
    top: 14px;
    width: 560px;
    height: 352px;
    border-radius: 6px;
    background: linear-gradient(135deg, rgba(26,26,26,0.22) 0%, rgba(143,193,60,0.35) 55%, rgba(217,233,76,0.25) 100%);
  }
  .services {
    position: absolute;
    left: 660px;
    top: 60px;
    list-style: none;
  }
  .services__item {
    display: flex;
    align-items: center;
    height: 64px;
    font-weight: 700;
    font-size: 62px;
    font-stretch: 115%;
    letter-spacing: 2px;
    color: var(--steel-gray);
    line-height: 1;
  }
  .services__item:nth-child(1) { padding-left: 20px; }
  .services__item:nth-child(2) { padding-left: 0; margin-top: 4px; }
  .services__item:nth-child(3) { padding-left: 6px; margin-top: 4px; }
  .services__tick { width: 42px; height: 36px; margin-right: 26px; flex: none; }
  .phone {
    position: absolute;
    left: 636px;
    top: 272px;
    font-weight: 800;
    font-size: 64px;
    font-stretch: 110%;
    letter-spacing: 2px;
    color: var(--ink);
    line-height: 1;
  }
  .brand-name {
    position: absolute;
    left: 310px;
    top: 374px;
    font-weight: 800;
    font-size: 60px;
    font-stretch: 125%;
    letter-spacing: 12px;
    text-transform: uppercase;
    color: var(--ink);
    line-height: 1;
  }
  .footer-band {
    position: absolute;
    left: 0;
    bottom: 0;
    width: 1200px;
    height: 110px;
    background: var(--ink);
    display: flex;
    align-items: center;
    justify-content: center;
  }
  .footer-band__name {
    font-weight: 600;
    font-size: 68px;
    font-stretch: 125%;
    letter-spacing: 4px;
    color: var(--paper);
    line-height: 1;
    white-space: nowrap;
  }
</style>
</head>
<body>
  <main class="sign">
    <div class="sign__glow"></div>

    <div class="mascot-art" role="img" aria-label="Line-art illustration of a dog's head in profile, black strokes on green"></div>

    <ul class="services">
      <li class="services__item">
        <svg class="services__tick" viewBox="0 0 42 36" aria-hidden="true"><path d="M3 20 L15 31 L39 5" fill="none" stroke="var(--tick-green)" stroke-width="7" stroke-linecap="round" stroke-linejoin="round"/></svg>
        DAYCARE
      </li>
      <li class="services__item">
        <svg class="services__tick" viewBox="0 0 42 36" aria-hidden="true"><path d="M3 20 L15 31 L39 5" fill="none" stroke="var(--tick-green)" stroke-width="7" stroke-linecap="round" stroke-linejoin="round"/></svg>
        BOARDING
      </li>
      <li class="services__item">
        <svg class="services__tick" viewBox="0 0 42 36" aria-hidden="true"><path d="M3 20 L15 31 L39 5" fill="none" stroke="var(--tick-green)" stroke-width="7" stroke-linecap="round" stroke-linejoin="round"/></svg>
        LEARNING
      </li>
    </ul>

    <p class="phone">319-555-0187</p>

    <h1 class="brand-name">Bright Paws</h1>

    <footer class="footer-band">
      <p class="footer-band__name">Hound Play Lodge LLC</p>
    </footer>
  </main>
</body>
</html>
```